Sports hypnotherapist needs electronic letterhead design

Need a simple but classy design for a letterhead that looks good when printed. Its for a hypnotherapist who specialises in elite sport. Should have my company name and address and website details on it. I specialise in footballers.
Should look good electronically and when printed.
Include all contact details as shown in the must haves.

Target Market(s)

Sports people, elite sport.

Industry/Entity Type

Hypnotherapy

Font styles to use
Sans Serif

Colors

Designer to choose colors to be used in the design.

Requirements
Must have
• NEEDS TO BE DESIGNED IN MS WORD
• Logo +
• Blue Heron Hypnotherapists
• 27 Marlowe Close
• Bracknell
• RG41 5PL
• Tel: 07700 900461
• E: blueheroncoaching@mailvale.com
• www: http://www.blue-heron-clinic.co.uk.
• Derek Ashworth
• Clinical hypnotherapist, hypnoanalyst, mental resilience coach, MSc, Dip PHH
Nice to have
• A watermark?
• Plenty of space for the A4 letter
• Prints well.
Should not have
• Too much clutter.
• Too much colour that will be costly to print.

```html
<!DOCTYPE html>
<html lang="en">
<head>
<meta charset="utf-8">
<title>Blue Heron Hypnotherapists – Letterhead</title>
<link href="https://fonts.googleapis.com/css2?family=Open+Sans:wght@400;600;700&family=Montserrat:wght@700&display=swap" rel="stylesheet">
<style>
  :root {
    --backdrop: #e4e4e4;
    --paper: #f3f3f3;
    --ink: #1a1a1a;
    --muted: #3a3a3a;
    --accent: #27aee3;
    --band: #111111;
    --watermark: #d6d6d6;
  }
  * { box-sizing: border-box; margin: 0; padding: 0; }
  html, body { width: 1200px; height: 891px; overflow: hidden; }
  body {
    background: var(--backdrop);
    font-family: "Open Sans", Arial, sans-serif;
    color: var(--ink);
    position: relative;
  }
  .letterhead {
    position: absolute;
    left: 300px; top: 20px;
    width: 600px; height: 850px;
    background: var(--paper);
    box-shadow: 0 4px 18px rgba(0,0,0,0.12);
    overflow: hidden;
  }
  .top-accent {
    position: absolute; left: 200px; top: 0;
    width: 180px; height: 6px;
    background: var(--accent);
  }
  .brand {
    position: absolute; left: 200px; top: 48px;
    display: flex; align-items: center; gap: 10px;
  }
  .brand-dot {
    width: 14px; height: 14px; border-radius: 50%;
    background: var(--accent);
  }
  .brand-name {
    font-family: "Montserrat", "Open Sans", sans-serif;
    font-weight: 700; font-size: 26px; color: var(--ink);
    letter-spacing: -0.3px;
  }
  .watermark {
    position: absolute; left: 200px; top: 200px;
    width: 220px; height: 420px;
    border-radius: 90px 90px 40px 40px;
    background: linear-gradient(180deg, var(--watermark), #e2e6e8);
    opacity: 0.75;
  }
  .letter {
    position: absolute; left: 60px; top: 230px; width: 470px;
    font-size: 10px; line-height: 14px; color: var(--muted);
  }
  .letter p { margin-bottom: 14px; }
  .letter .ref { margin-bottom: 16px; }
  .letter .recipient { margin-left: 20px; margin-bottom: 18px; }
  .letter .body { margin-left: 40px; }
  .closing { margin-top: 10px; }
  .signature {
    display: block; width: 200px; height: 60px; margin-top: 6px;
    border-radius: 30px;
    background: linear-gradient(90deg, #dcdcdc, #e8e8e8);
  }
  .footer-rule {
    position: absolute; left: 170px; right: 40px; top: 728px;
    height: 1px; background: #bdbdbd;
  }
  .footer-credentials {
    position: absolute; left: 170px; top: 738px;
    font-size: 9px; color: var(--ink);
  }
  .footer-credentials .name { color: var(--accent); font-weight: 700; }
  .footer-address {
    position: absolute; left: 150px; top: 756px;
    font-size: 9px; color: var(--ink);
    display: flex; align-items: center; gap: 4px;
  }
  .footer-address .practice { color: var(--accent); font-weight: 600; }
  .footer-contacts {
    position: absolute; right: 40px; top: 772px;
    font-size: 8.5px; display: flex; gap: 14px;
  }
  .footer-contacts span { display: flex; align-items: center; gap: 4px; }
  .bottom-band {
    position: absolute; left: 0; right: 0; top: 808px;
    height: 16px; background: var(--band);
  }
  .web-tab {
    position: absolute; right: 40px; top: 790px;
    width: 170px; height: 20px;
    background: var(--accent); color: #fff;
    font-size: 9px; display: flex; align-items: center; justify-content: center;
  }
  .icon { width: 9px; height: 9px; fill: var(--accent); }
</style>
</head>
<body>
  <main class="letterhead">
    <div class="top-accent"></div>

    <div class="brand">
      <span class="brand-dot"></span>
      <span class="brand-name">Blue Heron</span>
    </div>

    <div class="watermark" role="img" aria-label="Faint watermark of two athletes in silhouette"></div>

    <section class="letter">
      <p class="ref">Ref. No. ABC/123/2017<br>Dated: Dec 31, 2099</p>
      <p class="recipient">Mr. Graham Pellow<br>Director, Sales and Marketing<br>Northgate Holdings Limited<br>88 Linden Park Road, Leeds, LS2 7QT</p>
      <div class="body">
        <p>Dear Sir,</p>
        <p>Lorem ipsum dolor sit amet, consectetur adipiscing elit. Fusce nisl metus, tempus sit amet auctor non, eleifend sit amet metus. Cras ante nibh, adipiscing in sodales at, semper at augue. Duis dictum posuere dolor, sed interdum massacinia arcu. Duis laoreet nisl eget lectus sodales id mollis augue facilisis. Nam interdum purus sed ante tincidunt elementum facilisis non diam. Vestibuluneque, vel fermentum dui. Aliquam lacinia malesuada laoreet. Nunc mollis, ligula ac volutpat venenatis, dui diam consequat quam, in tincidunt elit risus at dui.</p>
        <p>Nulla ut neque justo, et ultrices velit. Nam convallis fermentum suscipit. Donec fringilla bibendum viverra. Vivamus dui tellus, sodales id faucibus at, aliquet ut libero. Praesent dapibus dui eget elit pretium ornare. Pellentesque hsa ut erat. Sed luctus ultrices arcu eu vestibulum.</p>
        <p>Nunc in nulla vitae magna venenatis condimentum. Quisque in bibendum tortor. Donec consequat hendrerit enim auctor dictum. Morbi augue mi, sodales nec tempus quis, ornare ut risus. Ut sit amet metus dolor, ac egestas purus. Pellentesque habitant morbi tristique senectus et netus et malesudunt. Nulla id cursus turpis.</p>
        <p class="closing">Your Sincerely as always</p>
        <span class="signature" role="img" aria-label="Handwritten signature of Adrian Cole"></span>
      </div>
    </section>

    <div class="footer-rule"></div>
    <p class="footer-credentials"><span class="name">Derek Ashworth</span> | Clinical hypnotherapist, hypnoanalyst, mental resilience coach, MSc, Dip PH</p>
    <p class="footer-address">
      <svg class="icon" viewBox="0 0 10 10"><path d="M5 0a3.5 3.5 0 0 0-3.5 3.5C1.5 6 5 10 5 10s3.5-4 3.5-6.5A3.5 3.5 0 0 0 5 0zm0 5a1.5 1.5 0 1 1 0-3 1.5 1.5 0 0 1 0 3z"/></svg>
      <span class="practice">Blue Heron Hypnotherapists:</span> 27 Marlowe Close, Bracknell, RG41 5PL
    </p>
    <div class="footer-contacts">
      <span><svg class="icon" viewBox="0 0 10 10"><path d="M2 0.5l2 2-1 1.2c.6 1.3 1.5 2.2 2.8 2.8l1.2-1 2 2-1.3 1.8C4 9 1 6 0.2 1.8z"/></svg>07700 900461</span>
      <span><svg class="icon" viewBox="0 0 10 10"><path d="M0 2h10v6H0zM0 2l5 3.5L10 2" stroke="#f3f3f3" stroke-width=".8"/></svg>blueheroncoaching@mailvale.com</span>
    </div>
    <div class="bottom-band"></div>
    <div class="web-tab">www.blue-heron-clinic.co.uk</div>
  </main>
</body>
</html>
```